Polystyrene Recycling Material Flow

We need a diagram styled as an infographic that shows how polystyrene foam is recycled starting with a manufactured product, moving through the distribution process, waste material collection and reincorporation back into manufacturing. This is accomplished in different ways once the material is collected which needs to be clearly evident. The most important thing is for it to be simple enough to understand while still having a stylish look. The design can be with or without vector images or photography to depict the different stages. We are providing a very rudimentary 'sketch' of the information points and movement flow. Please see www.foamtradeunion.org (resources) to view our literature branding. The RGB & CMYK are attached.

Target Market(s)

Government Agencies, Brand Owners, Retailers, Recycling Industry

Industry/Entity Type

Packaging, Recycling, Manufacturing

Font styles to use
Sans Serif

Requirements
Must have
• Easy to Understand
Nice to have
• Images - either photography or vector illustrations - are optional. We have provided examples of both to show what could be used but are not required. Substituting your own interpretation of imagery is encouraged.
Should not have
• Outdated look.

```html
<!DOCTYPE html>
<html lang="en">
<head>
<meta charset="utf-8">
<title>Polystyrene Recycling Material Flow</title>
<link rel="stylesheet" href="https://fonts.googleapis.com/css2?family=Barlow+Semi+Condensed:wght@500;600;700&family=Barlow:wght@400;500&display=swap">
<style>
  :root{
    --green:#8fa43a;
    --green-deep:#7f9530;
    --blue:#50809f;
    --blue-deep:#456f8d;
    --orange:#f7a21c;
    --orange-deep:#f39a12;
    --brown:#5b2c17;
    --brown-text:#5a2d14;
    --white:#ffffff;
    --head:"Barlow Semi Condensed", "Arial Narrow", sans-serif;
    --body:"Barlow", Arial, sans-serif;
  }
  *{margin:0;padding:0;box-sizing:border-box}
  html,body{width:1200px;height:724px;overflow:hidden;background:var(--white)}
  .canvas{position:relative;width:1200px;height:724px;overflow:hidden;color:var(--white)}
  .backdrop{position:absolute;inset:0}
  .t{position:absolute;white-space:nowrap;line-height:1}
  .section-title{font-family:var(--head);font-weight:700;font-size:31px;letter-spacing:.3px}
  .item{font-family:var(--head);font-weight:700;font-size:20.5px;letter-spacing:.2px}
  .sub{font-family:var(--body);font-weight:400;font-size:16.5px}
  .center{transform:translateX(-50%)}
  .collection-label{font-family:var(--head);font-weight:700;font-size:28px;color:var(--brown-text);letter-spacing:.5px}
  .check{position:absolute;width:20px;height:20px;border-radius:50%;background:var(--white)}
  .check::after{content:"";position:absolute;left:6px;top:4px;width:5px;height:9px;border:solid var(--tick);border-width:0 3px 3px 0;transform:rotate(45deg)}
  .on-green{--tick:var(--green)}
  .on-orange{--tick:var(--orange)}
  .on-blue{--tick:var(--blue)}
  .chev{position:absolute;width:7px;height:7px;border:solid var(--white);border-width:1.5px 1.5px 0 0;transform:rotate(45deg)}
  .chev.back{transform:rotate(-135deg)}
  .art{position:absolute}
  .art-truck{left:47px;top:73px;width:150px;height:99px;border-radius:10px;background:linear-gradient(160deg,#9be23c,#5fae1f)}
  .art-bin{left:548px;top:50px;width:104px;height:42px;border-radius:6px;background:linear-gradient(180deg,#8a4a22,#4b2410)}
  .art-sign{left:540px;top:240px;width:120px;height:107px;border-radius:6px;background:linear-gradient(180deg,#ffffff,#dfe9e4)}
  .art-pellets{left:870px;top:73px;width:133px;height:103px;border-radius:50%;background:radial-gradient(circle at 50% 45%,#ffffff,#d9dfe3)}
</style>
</head>
<body>
<main class="canvas">
  <svg class="backdrop" width="1200" height="724" viewBox="0 0 1200 724" aria-hidden="true">
    <defs>
      <linearGradient id="greenField" x1="0" y1="0" x2="0" y2="1">
        <stop offset="0" stop-color="var(--green)"/><stop offset="1" stop-color="var(--green-deep)"/>
      </linearGradient>
      <linearGradient id="blueField" x1="0" y1="0" x2="0" y2="1">
        <stop offset="0" stop-color="var(--blue)"/><stop offset="1" stop-color="var(--blue-deep)"/>
      </linearGradient>
      <linearGradient id="orangeField" x1="0" y1="0" x2="0" y2="1">
        <stop offset="0" stop-color="var(--orange-deep)"/><stop offset="1" stop-color="var(--orange)"/>
      </linearGradient>
    </defs>
    <rect x="0" y="0" width="600" height="724" fill="url(#greenField)"/>
    <rect x="600" y="0" width="600" height="724" fill="url(#blueField)"/>
    <polygon points="437,146 763,146 887,724 313,724" fill="url(#orangeField)"/>
    <g stroke="#fff" stroke-width="1" stroke-dasharray="2 3" fill="none" opacity=".9">
      <line x1="437" y1="146" x2="313" y2="724"/>
      <line x1="763" y1="146" x2="887" y2="724"/>
      <line x1="47" y1="302" x2="273" y2="302"/>
      <line x1="47" y1="450" x2="334" y2="450"/>
      <line x1="47" y1="515" x2="300" y2="515"/>
      <line x1="351" y1="558" x2="441" y2="558"/>
      <line x1="422" y1="495" x2="769" y2="495"/>
      <line x1="422" y1="665" x2="769" y2="665"/>
      <line x1="871" y1="345" x2="1095" y2="345"/>
      <line x1="844" y1="525" x2="1191" y2="525"/>
    </g>
    <circle cx="600" cy="34" r="219" fill="var(--brown)"/>
    <circle cx="600" cy="34" r="167" fill="#fff"/>
    <g>
      <circle cx="402" cy="319" r="14" fill="#fff"/>
      <path d="M402 325v-10m-4 4l4-4 4 4" stroke="var(--orange)" stroke-width="2.2" fill="none" stroke-linecap="round"/>
      <circle cx="799" cy="319" r="14" fill="#fff"/>
      <path d="M799 325v-10m-4 4l4-4 4 4" stroke="var(--blue)" stroke-width="2.2" fill="none" stroke-linecap="round"/>
    </g>
  </svg>

  <div class="art art-truck" role="img" aria-label="Green refuse collection truck"></div>
  <div class="art art-bin" role="img" aria-label="Brown recycling collection bin"></div>
  <div class="art art-sign" role="img" aria-label="Recycle here sign"></div>
  <div class="art art-pellets" role="img" aria-label="Bowl of white polystyrene beads"></div>

  <p class="t collection-label center" style="left:600px;top:104px">COLLECTION</p>

  <!-- Waste sources -->
  <section>
    <h2 class="t section-title" style="left:45px;top:208px">EPS WASTE SOURCES</h2>
    <span class="check on-green" style="left:47px;top:266px"></span>
    <p class="t item" style="left:83px;top:266px">MUNICIPAL WASTE</p>
    <span class="chev" style="left:66px;top:332px"></span>
    <p class="t sub" style="left:84px;top:326px">Curbside Collection</p>
    <span class="chev" style="left:66px;top:369px"></span>
    <p class="t sub" style="left:84px;top:363px">Drop-Off Centers</p>
    <span class="check on-green" style="left:47px;top:414px"></span>
    <p class="t item" style="left:83px;top:414px">MANUFACTURING WASTE</p>
    <span class="check on-green" style="left:47px;top:479px"></span>
    <p class="t item" style="left:83px;top:479px">COMMERCIAL WASTE</p>
    <span class="chev" style="left:66px;top:546px"></span>
    <p class="t sub" style="left:84px;top:540px">Back Hauling</p>
    <span class="chev" style="left:66px;top:583px"></span>
    <p class="t sub" style="left:84px;top:577px">Localized Delivery</p>
  </section>

  <!-- Compaction -->
  <section>
    <h2 class="t section-title center" style="left:600px;top:371px">COMPACTION</h2>
    <p class="t sub" style="left:419px;top:415px">Extruded Ingot</p>
    <p class="t sub" style="left:567px;top:413px">|</p>
    <p class="t sub" style="left:601px;top:415px">Hydrolic Compression</p>
    <span class="check on-orange" style="left:421px;top:457px"></span>
    <p class="t item" style="left:458px;top:457px">RECYCLEDCONTENT EPS RESIN</p>
    <span class="chev" style="left:436px;top:521px"></span>
    <p class="t sub" style="left:458px;top:515px">Re-Pelletized With Blowing Agent</p>
    <span class="chev back" style="left:441px;top:555px"></span>
    <p class="t sub" style="left:458px;top:549px">Expanded Polystyrene Packaging &amp; Building</p>
    <p class="t sub" style="left:458px;top:583px">Products &lt;50%</p>
    <span class="check on-orange" style="left:421px;top:627px"></span>
    <p class="t item" style="left:458px;top:627px">EXTRUDED RIGID PS PELLET</p>
    <p class="t sub" style="left:458px;top:684px">End Market Applications</p>
  </section>

  <!-- Regrind-molder -->
  <section>
    <h2 class="t section-title" style="left:869px;top:199px">REGRIND-</h2>
    <h2 class="t section-title" style="left:869px;top:244px">MOLDER FACILITIES</h2>
    <span class="check on-blue" style="left:870px;top:305px"></span>
    <p class="t item" style="left:907px;top:305px">SHREDDING</p>
    <span class="chev" style="left:889px;top:372px"></span>
    <p class="t sub" style="left:908px;top:366px">Homogenization</p>
    <span class="chev" style="left:889px;top:409px"></span>
    <p class="t sub" style="left:908px;top:403px">Mixing for Consistency</p>
    <span class="check on-blue" style="left:870px;top:454px"></span>
    <p class="t item" style="left:907px;top:454px">RECYCLED</p>
    <p class="t item" style="left:907px;top:485px">CONTENT PACKAGING &lt;15%</p>
    <span class="chev back" style="left:1187px;top:522px"></span>
  </section>
</main>
</body>
</html>
```